Vape Brand Cartoon Packaging Design

I AM NOT PICKY!! Just need to get the basic job done and I will be happy. To start we need a text logo for our brand "Mira Frost" vape cartridges that is colorful, with a cartoonish design. We have 3 flavors we are starting with that need there own custom logo: Lilac Drizzle (colorful pink packaging with ice cream sherbert incorporated in the cartoon design), Velvet Anchor (blue background with a white cake cartoon design), and Marble Dingo (orange packaging with cartoon animated zumbo cookies acting crazy/fighting on it). I dont care if the images are sourced from yondo images or wherever. See the uploaded files for guidance I want them extremely similar to that packaging. The packaging is roughly 1.5 inches wide and 2.5 inches tall.
Where the packaging says "north ridge rarities" I want my brand name "Mira Frost", underneath it I want it to say "vape cartridge" just like in the picture. I also want the flavors in the same area on the package and for them all to say HYBRID and 1.0 gram in the same spot. Instead of 1.0 gram though have it say 1000 mg. To reiterate I want the packaging very similar to the packaging in the picture. There will be other flavors added in the near future so ideally I want someone I can work with in the long term!
Mira Frost

```html
<!DOCTYPE html>
<html lang="en">
<head>
<meta charset="utf-8">
<title>Mira Frost Vape Cartridge Packaging</title>
<link href="https://fonts.googleapis.com/css2?family=Rye&family=Arimo:wght@700&display=swap" rel="stylesheet">
<style>
  :root {
    --canvas: #fde7c6;
    --canvas-dot: #fbdcb2;
    --brand-orange: #e8801c;
    --tagline-orange: #f05a28;
    --pink-light: #f6bcd9;
    --pink-mid: #ec8fc0;
    --pink-drip: #b9588f;
    --pink-ink: #e0147e;
    --pink-brand: #d13f86;
    --orange-light: #f8b04a;
    --orange-mid: #f09026;
    --orange-ink: #3a2410;
    --orange-brand: #7a3a10;
    --blue-light: #6f7fd0;
    --blue-mid: #4353ad;
    --blue-ink: #1c1a38;
    --blue-brand: #1f5fb8;
    --title-fill: #ffffff;
    --title-edge: #3b1320;
  }
  * { box-sizing: border-box; margin: 0; padding: 0; }
  html, body { width: 1200px; height: 1000px; overflow: hidden; }
  body {
    position: relative;
    background: radial-gradient(circle at 30% 30%, var(--canvas-dot) 0 18px, transparent 19px) 0 0 / 60px 60px, var(--canvas);
    font-family: "Arimo", Arial, sans-serif;
  }
  .brand-header { position: absolute; left: 40px; top: 30px; width: 755px; text-align: center; }
  .brand-name {
    font-family: "Rye", serif; font-size: 94px; line-height: 150px;
    color: var(--brand-orange); letter-spacing: 1px; white-space: nowrap; font-weight: 400;
  }
  .brand-tagline {
    position: absolute; left: 60px; top: 198px; width: 715px; text-align: center;
    font-size: 30px; line-height: 36px; color: var(--tagline-orange); font-weight: 700; white-space: nowrap;
  }

  .pack {
    position: absolute; width: 362px; height: 604px; overflow: hidden;
    text-align: center;
  }
  .pack-lilac { background: linear-gradient(180deg, var(--pink-light), var(--pink-mid)); }
  .pack-marble { background: linear-gradient(180deg, var(--orange-light), var(--orange-mid)); }
  .pack-velvet { background: radial-gradient(ellipse at 50% 40%, var(--blue-light), var(--blue-mid)); }

  .drip-band { position: absolute; left: 0; top: 0; width: 100%; height: 40px; }

  .flavor-title {
    position: absolute; left: 0; top: 36px; width: 100%;
    font-family: "Rye", serif; font-size: 36px; line-height: 42px; font-weight: 400;
    color: var(--title-fill); white-space: nowrap;
    text-shadow: 2px 2px 0 var(--title-edge), -2px 2px 0 var(--title-edge), 2px -2px 0 var(--title-edge), -2px -2px 0 var(--title-edge), 4px 4px 0 var(--title-edge);
  }
  .pack-brand {
    position: absolute; left: 0; top: 150px; width: 100%;
    font-family: "Rye", serif; font-size: 44px; line-height: 64px; white-space: nowrap;
  }
  .pack-lilac .pack-brand { color: var(--pink-brand); }
  .pack-marble .pack-brand { color: var(--orange-brand); }
  .pack-velvet .pack-brand { color: var(--blue-brand); }

  .pack-tagline { position: absolute; left: 0; top: 226px; width: 100%; font-size: 14px; font-weight: 700; }
  .pack-artwork { position: absolute; left: 70px; top: 262px; width: 222px; height: 270px; border-radius: 18px; }
  .pack-strain { position: absolute; left: 0; top: 544px; width: 100%; font-size: 20px; line-height: 22px; font-weight: 700; }
  .pack-weight { position: absolute; left: 0; top: 569px; width: 100%; font-size: 15px; line-height: 18px; font-weight: 700; }

  .pack-lilac .pack-tagline, .pack-lilac .pack-strain, .pack-lilac .pack-weight { color: var(--pink-ink); }
  .pack-marble .pack-tagline, .pack-marble .pack-strain, .pack-marble .pack-weight { color: var(--orange-ink); }
  .pack-velvet .pack-tagline, .pack-velvet .pack-strain, .pack-velvet .pack-weight { color: var(--blue-ink); }

  .pack-lilac .pack-artwork { background: radial-gradient(circle at 50% 45%, #f4d26a, #ec86b4 55%, #e24f9a); }
  .pack-marble .pack-artwork { background: radial-gradient(circle at 50% 45%, #e9cfa4, #b5763a 60%, #f09026); }
  .pack-velvet .pack-artwork { background: linear-gradient(180deg, #d9b58a, #ffffff 25%, #f6e6d6 75%, #c9c9d6); }

  .pack-full-lilac { left: 32px; top: 284px; }
  .pack-full-marble { left: 423px; top: 288px; }
  .pack-full-velvet { left: 812px; top: 288px; }

  .pack-thumb { transform-origin: 0 0; transform: scale(0.298); }
  .pack-thumb-lilac { left: 822px; top: 42px; }
  .pack-thumb-marble { left: 945px; top: 42px; }
  .pack-thumb-velvet { left: 1066px; top: 42px; }
</style>
</head>
<body>
  <header class="brand-header">
    <h1 class="brand-name">MIRA FROST</h1>
  </header>
  <p class="brand-tagline">VAPE CARTRIDGE</p>

  <section class="pack pack-lilac pack-thumb pack-thumb-lilac">
    <svg class="drip-band" viewBox="0 0 362 40" preserveAspectRatio="none"><path d="M0 0H362V14Q340 14 335 30Q330 14 300 14Q280 14 275 34Q270 14 240 14Q220 14 215 26Q210 14 180 14Q160 14 155 36Q150 14 120 14Q100 14 95 28Q90 14 60 14Q40 14 35 32Q30 14 0 14Z" fill="#b9588f"/></svg>
    <h2 class="flavor-title">LILAC<br>DRIZZLE</h2>
    <p class="pack-brand">MIRA FROST</p>
    <p class="pack-tagline">VAPE CARTRIDGE</p>
    <div class="pack-artwork" role="img" aria-label="Cartoon stack of smiling sherbet scoops on a pink dish"></div>
    <p class="pack-strain">HYBRID</p>
    <p class="pack-weight">1000 MG</p>
  </section>
  <section class="pack pack-marble pack-thumb pack-thumb-marble">
    <h2 class="flavor-title">MARBLE<br>DINGO</h2>
    <p class="pack-brand">MIRA FROST</p>
    <p class="pack-tagline">VAPE CARTRIDGE</p>
    <div class="pack-artwork" role="img" aria-label="Cartoon mug of cocoa with lively zumbo cookies scuffling around it"></div>
    <p class="pack-strain">HYBRID</p>
    <p class="pack-weight">1000 MG</p>
  </section>
  <section class="pack pack-velvet pack-thumb pack-thumb-velvet">
    <h2 class="flavor-title">VELVET<br>ANCHOR</h2>
    <p class="pack-brand">MIRA FROST</p>
    <p class="pack-tagline">VAPE CARTRIDGE</p>
    <div class="pack-artwork" role="img" aria-label="Cartoon three tier white cake with cream swags"></div>
    <p class="pack-strain">HYBRID</p>
    <p class="pack-weight">1000 MG</p>
  </section>

  <section class="pack pack-lilac pack-full-lilac">
    <svg class="drip-band" viewBox="0 0 362 40" preserveAspectRatio="none"><path d="M0 0H362V14Q340 14 335 30Q330 14 300 14Q280 14 275 34Q270 14 240 14Q220 14 215 26Q210 14 180 14Q160 14 155 36Q150 14 120 14Q100 14 95 28Q90 14 60 14Q40 14 35 32Q30 14 0 14Z" fill="#b9588f"/></svg>
    <h2 class="flavor-title">LILAC<br>DRIZZLE</h2>
    <p class="pack-brand">MIRA FROST</p>
    <p class="pack-tagline">VAPE CARTRIDGE</p>
    <div class="pack-artwork" role="img" aria-label="Cartoon stack of smiling sherbet scoops on a pink dish"></div>
    <p class="pack-strain">HYBRID</p>
    <p class="pack-weight">1000 MG</p>
  </section>
  <section class="pack pack-marble pack-full-marble">
    <h2 class="flavor-title">MARBLE<br>DINGO</h2>
    <p class="pack-brand">MIRA FROST</p>
    <p class="pack-tagline">VAPE CARTRIDGE</p>
    <div class="pack-artwork" role="img" aria-label="Cartoon mug of cocoa with lively zumbo cookies scuffling around it"></div>
    <p class="pack-strain">HYBRID</p>
    <p class="pack-weight">1000 MG</p>
  </section>
  <section class="pack pack-velvet pack-full-velvet">
    <h2 class="flavor-title">VELVET<br>ANCHOR</h2>
    <p class="pack-brand">MIRA FROST</p>
    <p class="pack-tagline">VAPE CARTRIDGE</p>
    <div class="pack-artwork" role="img" aria-label="Cartoon three tier white cake with cream swags"></div>
    <p class="pack-strain">HYBRID</p>
    <p class="pack-weight">1000 MG</p>
  </section>
</body>
</html>
```